K. Morendi needs an original business card for property investment professionals

The business card would be to present me as an investor in the real estate business. The market are developers of real estate projects, or other people who would like to sell and also to give us a name as a company. For style, colour and imagery I would like something artistic from Morendi (the artist) with a different touch.

Address, email, cel phone,
Updates

Hi¡ Update¡ I;d like it to stop providing Bright Acre as a Design and focus in K.Morendi.

Target Market(s)

Real Estate Developer/Investor

Industry/Entity Type

Real Estate

Colors
33a6d7
886aae
e3daeb
cadf82
f78f20

```html
<!DOCTYPE html>
<html lang="en">
<head>
<meta charset="utf-8">
<title>K.Morendi – Business Card</title>
<link href="https://fonts.googleapis.com/css2?family=Open+Sans:wght@400;600&display=swap" rel="stylesheet">
<style>
  :root {
    --backdrop: #e4e4e6;
    --card-white: #f7f7f5;
    --ink: #5b3b3a;
    --night-deep: #2e1634;
    --night-teal: #1d5650;
    --night-green: #24664a;
    --window-glow: #f2d21c;
    --art-red: #e32a2a;
    --art-green: #1e9a3c;
    --art-blue: #2a5fc8;
    --art-orange: #f78f20;
    --art-lilac: #b7a6dc;
    --title-white: #f4f1f4;
  }
  * { margin: 0; padding: 0; box-sizing: border-box; }
  html, body {
    width: 1200px;
    height: 800px;
    overflow: hidden;
    background: var(--backdrop);
  }
  .canvas {
    position: relative;
    width: 1200px;
    height: 800px;
    display: flex;
    align-items: center;
    justify-content: center;
    gap: 60px;
  }
  .card {
    position: relative;
    width: 500px;
    height: 290px;
    overflow: hidden;
    box-shadow: 0 6px 18px rgba(0, 0, 0, 0.12);
  }

  /* Front: contact side */
  .card-front {
    background: var(--card-white);
  }
  .contact-block {
    position: absolute;
    left: 34px;
    top: 44px;
    color: var(--ink);
    font-family: "Open Sans", sans-serif;
  }
  .holder-name {
    font-size: 27px;
    font-weight: 400;
    letter-spacing: 0.5px;
    line-height: 1;
  }
  .company-line {
    font-size: 10px;
    margin-top: 4px;
    margin-bottom: 14px;
  }
  .contact-line {
    font-size: 18px;
    line-height: 1.28;
  }
  .front-art {
    position: absolute;
    right: 0;
    top: 0;
    width: 205px;
    height: 100%;
    background:
      radial-gradient(circle at 30% 70%, var(--art-red) 0 18%, transparent 40%),
      radial-gradient(circle at 75% 35%, var(--art-green) 0 15%, transparent 38%),
      radial-gradient(circle at 60% 85%, var(--art-blue) 0 12%, transparent 35%),
      radial-gradient(circle at 20% 20%, var(--art-lilac) 0 15%, transparent 40%),
      linear-gradient(160deg, var(--art-orange), var(--art-red) 45%, var(--art-green));
  }

  /* Back: brand side */
  .card-back {
    background:
      radial-gradient(ellipse at 40% 65%, rgba(242, 210, 28, 0.22), transparent 55%),
      linear-gradient(160deg, var(--night-deep) 0%, var(--night-deep) 28%, var(--night-teal) 60%, var(--night-green) 100%);
  }
  .back-art {
    position: absolute;
    inset: 0;
  }
  .brand-name {
    position: absolute;
    left: 0;
    right: 0;
    top: 50%;
    transform: translateY(-50%);
    text-align: center;
    color: var(--title-white);
    font-family: "Open Sans", sans-serif;
    font-weight: 400;
    font-size: 40px;
    letter-spacing: 3px;
  }
</style>
</head>
<body>
  <main class="canvas">
    <section class="card card-front">
      <div class="contact-block">
        <p class="holder-name">DANIEL REYES</p>
        <p class="company-line">K.MORENDI ltd</p>
        <p class="contact-line">+10019876543</p>
        <p class="contact-line">hello@morendi.com</p>
        <p class="contact-line">4120 NW Harbor</p>
        <p class="contact-line">Lake st. 82 of.3</p>
      </div>
      <div class="front-art" role="img" aria-label="Colourful abstract stained-glass style artwork of overlapping curves in red, green, blue, orange and lilac"></div>
    </section>

    <section class="card card-back">
      <div class="back-art" role="img" aria-label="Stained-glass style night cityscape with lit yellow windows, teal buildings and a crescent moon on a deep purple sky"></div>
      <p class="brand-name">K.MORENDI</p>
    </section>
  </main>
</body>
</html>
```